New Business Card Design Project

I would like to purchase a customized version of a design you have previously submitted - https://www.plomarket.com/design/7724163<br/><br/>I would like to incorporate the attached Images for my fitness company "TalvrenPro Athletics". My initial services is personal training and athletic performance. I would like a card that has one a shiny black side with the silver logo and the side with a white background utilizing the gold logo. On the white side, put "Sports Performance and Functional Strength Training" under the logo.
Industry/Entity Type
Fitness
Contact Information for Business Card
Marcus Tolley
Owner and Trainer
555.273.8492
marcus.tolley@talvrenproathletics.com
Look and feel
Each slider illustrates characteristics of the customer's brand and the style your logo design should communicate.

```html
<!DOCTYPE html>
<html lang="en">
<head>
<meta charset="utf-8">
<title>TalvrenPro Athletics — Business Card</title>
<link href="https://fonts.googleapis.com/css2?family=Montserrat:wght@600;700&family=Arimo:wght@400;700&display=swap" rel="stylesheet">
<style>
  :root {
    --backdrop: #2b2b2d;
    --card-black: #0a0a0a;
    --card-white: #ffffff;
    --silver: #cfd0d2;
    --gold: #b39a6b;
    --ink: #1a1a1a;
    --light-text: #f2f2f2;
    --muted-text: #bdbdbd;
  }
  * { box-sizing: border-box; margin: 0; padding: 0; }
  html, body { width: 1200px; height: 880px; overflow: hidden; }
  body {
    background: var(--backdrop);
    font-family: "Arimo", Arial, sans-serif;
    position: relative;
  }
  .card {
    position: absolute;
    left: 250px;
    width: 700px;
    height: 400px;
    box-shadow: 0 10px 30px rgba(0,0,0,.45);
    overflow: hidden;
  }
  /* Front: shiny black with silver mark */
  .card-front {
    top: 26px;
    background: linear-gradient(120deg, #000 0%, #1c1c1c 42%, #050505 58%, #000 100%);
  }
  .front-mark {
    position: absolute;
    left: 50%; top: 50%;
    transform: translate(-50%, -50%);
    width: 230px; height: 230px;
    border-radius: 50%;
    border: 3px solid var(--silver);
    display: flex; align-items: center; justify-content: center;
    text-align: center;
  }
  .brand-name {
    font-family: "Montserrat", Arial, sans-serif;
    font-weight: 700;
    font-size: 24px;
    line-height: 1.25;
    letter-spacing: 2px;
    text-transform: uppercase;
  }
  .front-mark .brand-name { color: var(--silver); }

  /* Back: white with black band and gold mark */
  .card-back {
    top: 454px;
    background: var(--card-white);
  }
  .back-band { position: absolute; inset: 0; }
  .back-mark {
    position: absolute;
    left: 70px; top: 130px;
    width: 220px; height: 220px;
    border-radius: 50%;
    background: var(--card-white);
    border: 3px solid var(--gold);
    display: flex; align-items: center; justify-content: center;
    text-align: center;
  }
  .back-mark .brand-name { color: var(--gold); font-size: 22px; }
  .contact {
    position: absolute;
    left: 380px; top: 100px;
    color: var(--light-text);
    white-space: nowrap;
  }
  .contact-name {
    font-family: "Montserrat", Arial, sans-serif;
    font-weight: 700;
    font-size: 24px;
    line-height: 1.2;
    color: var(--gold);
  }
  .contact-title {
    font-size: 13px;
    letter-spacing: 1px;
    text-transform: uppercase;
    color: var(--muted-text);
    margin: 2px 0 10px;
  }
  .contact-line {
    display: flex; align-items: center;
    gap: 12px;
    font-size: 15px;
    margin-bottom: 6px;
  }
  .contact-line svg { flex: none; }
  .tagline {
    position: absolute;
    left: 300px; top: 274px;
    font-family: "Arimo", Arial, sans-serif;
    font-weight: 700;
    font-size: 13px;
    white-space: nowrap;
    color: var(--ink);
  }
</style>
</head>
<body>
  <section class="card card-front" aria-label="Card front">
    <div class="front-mark">
      <span class="brand-name">TalvrenPro<br>Athletics</span>
    </div>
  </section>

  <section class="card card-back" aria-label="Card back">
    <svg class="back-band" width="700" height="400" viewBox="0 0 700 400" aria-hidden="true">
      <path d="M190 120 L700 40 L700 230 L300 262 A120 120 0 0 0 190 120 Z" fill="var(--card-black)"/>
    </svg>
    <div class="back-mark">
      <span class="brand-name">TalvrenPro<br>Athletics</span>
    </div>
    <div class="contact">
      <p class="contact-name">Marcus Tolley</p>
      <p class="contact-title">Owner and Trainer</p>
      <p class="contact-line">
        <svg width="14" height="14" viewBox="0 0 14 14" aria-hidden="true"><rect x="1" y="1" width="12" height="12" fill="none" stroke="var(--light-text)" stroke-width="1.5"/></svg>
        555.273.8492
      </p>
      <p class="contact-line">
        <svg width="16" height="12" viewBox="0 0 16 12" aria-hidden="true"><rect x="0" y="0" width="16" height="12" fill="var(--gold)"/><path d="M0 0 L8 7 L16 0" fill="none" stroke="var(--card-black)" stroke-width="1.2"/></svg>
        marcus.tolley@talvrenproathletics.com
      </p>
    </div>
    <p class="tagline">Sports Performance and Functional Strength Training</p>
  </section>
</body>
</html>
```